Hi, We are global cloud printer looking to start a ad print run, we require full and half page print ad's designed with the following dimensions

Full page dimensions:

Image area: 345 mm in height x 260 mm (6 columns) in width
Trim area: 368 mm in height x 280 mm (6 columns) in width
Bleed area: 371 mm in height x 283 mm (6 columns) in width

Half-page dimensions:
270 mm in height x 172 mm (4 columns) in width

We want a minimalistic ad that really stands out from the crowd, with a full page we want it to make an impact and drive people towards our site.

The site is www.plaventro.com , we would like to match the look and feel but would like the wow factor so our open to all concepts.

We would like the following tagline incorporated in the Ad The cloud you've been waiting for, might be closer than you think.

```html
<!DOCTYPE html>
<html lang="en">
<head>
<meta charset="utf-8">
<title>Plaventro – Print Ad Set</title>
<link rel="stylesheet" href="https://fonts.googleapis.com/css2?family=Roboto:wght@400;700;900&display=swap">
<style>
  :root {
    --stage: #1e1e1e;
    --green: #72bf44;
    --tint: rgba(255, 255, 255, 0.07);
    --tint-strong: rgba(255, 255, 255, 0.1);
    --cloud: #f4f4f4;
    --ink: #474747;
    --white: #ffffff;
  }
  * { margin: 0; padding: 0; box-sizing: border-box; }
  html, body {
    width: 1200px;
    height: 800px;
    overflow: hidden;
    background: var(--stage);
    font-family: "Roboto", Arial, sans-serif;
  }
  .stage { position: relative; width: 1200px; height: 800px; }

  .ad {
    position: absolute;
    overflow: hidden;
    background: var(--green);
  }
  .ad--full { left: 20px; top: 29px; width: 556px; height: 740px; }
  .ad--half { left: 604px; top: 400px; width: 577px; height: 369px; }

  .ad__backdrop { position: absolute; inset: 0; width: 100%; height: 100%; }
  .ad__backdrop .glow { fill: var(--tint); }
  .ad__backdrop .glow--strong { fill: var(--tint-strong); }
  .ad__backdrop .cloud { fill: var(--cloud); }
  .ad__backdrop .rail, .ad__backdrop .peg { fill: var(--cloud); }

  .brand { position: absolute; text-align: center; }
  .brand__name {
    display: block;
    font-weight: 700;
    color: var(--ink);
    line-height: 1;
    letter-spacing: -0.01em;
  }
  .brand__rule { display: block; height: 1.5px; background: var(--ink); opacity: 0.75; }
  .brand__url {
    display: block;
    font-weight: 400;
    color: var(--ink);
    line-height: 1;
  }

  .headline, .subline, .closer, .closer-sub {
    position: absolute;
    line-height: 1;
    white-space: nowrap;
  }
  .headline, .closer { color: var(--white); font-weight: 700; letter-spacing: -0.01em; }
  .subline, .closer-sub { color: var(--ink); font-weight: 700; }

  .umbrella-slot {
    position: absolute;
    border-radius: 40% 40% 50% 50% / 18% 18% 82% 82%;
    background: linear-gradient(180deg, #f6f6f6 0%, #eef2ea 100%);
  }

  /* Full page */
  .ad--full .brand { left: 304px; top: 38px; width: 207px; }
  .ad--full .brand__name { font-size: 37px; }
  .ad--full .brand__rule { margin-top: 4px; }
  .ad--full .brand__url { font-size: 14px; margin-top: 6px; }
  .ad--full .headline { left: 161px; top: 236px; font-size: 50px; }
  .ad--full .subline { left: 163px; top: 283px; font-size: 18px; }
  .ad--full .umbrella-slot { left: 262px; top: 350px; width: 100px; height: 242px; }
  .ad--full .closer { left: 163px; top: 634px; font-size: 35px; }
  .ad--full .closer-sub { left: 229px; top: 669px; font-size: 18px; }

  /* Half page */
  .ad--half .brand { left: 405px; top: 30px; width: 140px; }
  .ad--half .brand__name { font-size: 26px; }
  .ad--half .brand__rule { margin-top: 4px; }
  .ad--half .brand__url { font-size: 12px; margin-top: 4px; }
  .ad--half .headline { left: 62px; top: 184px; font-size: 34px; }
  .ad--half .subline { left: 63px; top: 216px; font-size: 13px; }
  .ad--half .umbrella-slot { left: 278px; top: 158px; width: 72px; height: 170px; }
  .ad--half .closer { left: 376px; top: 289px; font-size: 24px; }
  .ad--half .closer-sub { left: 420px; top: 312px; font-size: 12px; }
</style>
</head>
<body>
<main class="stage">

  <section class="ad ad--full" aria-label="Full page ad">
    <svg class="ad__backdrop" viewBox="0 0 556 740" aria-hidden="true">
      <circle class="glow" cx="-140" cy="930" r="720"/>
      <circle class="glow--strong" cx="560" cy="940" r="440"/>
      <circle class="cloud" cx="287" cy="-80" r="247"/>
      <circle class="cloud" cx="535" cy="80" r="120"/>
      <rect class="rail" x="129" y="325" width="298" height="7"/>
      <circle class="peg" cx="173" cy="357" r="6"/>
      <circle class="peg" cx="245" cy="357" r="6"/>
      <circle class="peg" cx="383" cy="357" r="6"/>
    </svg>
    <div class="brand">
      <span class="brand__name">plaventro</span>
      <span class="brand__rule"></span>
      <span class="brand__url">www.plaventro.com</span>
    </div>
    <h1 class="headline">The cloud</h1>
    <p class="subline">you've been waiting for.</p>
    <div class="umbrella-slot" role="img" aria-label="Closed white umbrella hanging from the rail by its hook"></div>
    <h2 class="closer">Might be closer</h2>
    <p class="closer-sub">than you think.</p>
  </section>

  <section class="ad ad--half" aria-label="Half page ad">
    <svg class="ad__backdrop" viewBox="0 0 577 369" aria-hidden="true">
      <circle class="glow" cx="-120" cy="560" r="560"/>
      <circle class="glow--strong" cx="560" cy="560" r="330"/>
      <circle class="cloud" cx="340" cy="-80" r="173"/>
      <circle class="cloud" cx="513" cy="33" r="113"/>
      <rect class="rail" x="193" y="143" width="202" height="5"/>
      <circle class="peg" cx="223" cy="167" r="4"/>
      <circle class="peg" cx="271" cy="167" r="4"/>
      <circle class="peg" cx="365" cy="167" r="4"/>
    </svg>
    <div class="brand">
      <span class="brand__name">plaventro</span>
      <span class="brand__rule"></span>
      <span class="brand__url">www.plaventro.com</span>
    </div>
    <h1 class="headline">The cloud</h1>
    <p class="subline">you've been waiting for.</p>
    <div class="umbrella-slot" role="img" aria-label="Closed white umbrella hanging from the rail by its hook"></div>
    <h2 class="closer">Might be closer</h2>
    <p class="closer-sub">than you think.</p>
  </section>

</main>
</body>
</html>
```